Pat Greene Billboard

**Task Description: Billboard Design for Self Storage Facility**

**Objective:**
Design a captivating billboard to promote our self-storage facility with a focus on our convenient location and online rental capabilities.

**Key Messages to Include:**
1. **Location Emphasis:** Highlight that our facility is located right beside the billboard (maybe by using an arrow pointing left).
2. **Online Rental Convenience:** Feature prominently that customers can "Rent Online Anytime!” or that we are "Always Open Online!"

**Target Audience:**
- Local residents looking for convenient self-storage solutions.
- Businesses needing storage space accessible around the clock.

**Design Elements:**
1. **Visual Impact:** Eye-catching graphics and colors that stand out against the surroundings.
2. **Clear Text:** Bold and concise messaging that can be read and understood quickly.
3. **Contact Information:** Include our phone number and website URL for easy access to further information.

**Additional Information:**
- Billboard dimensions: 12 ft. x 24 ft.
- Preferred color scheme: Bright and attention-grabbing, but professional.
- Branding: Incorporate our logo and brand colors to maintain consistency.

**Deliverables:**
- High-resolution digital file compatible with billboard printing specifications.
- Consider mockups or visualizations for presentation purposes.

Please note that I have attached current logos/graphics that we would love to incorporate into the billboard as well as a picture of our current billboard. Our logo (Pat Greene Self Storage - PG navy.png) MUST be incorporated into the billboard. Also feel free to add any of the current descriptions from the picture of our current billboard into the design. Instead of using "Climate Controlled" use "Temperature Controlled". Thank you for your attention to these details. We look forward to reviewing your proposed design!

```html
<!DOCTYPE html>
<html lang="en">
<head>
<meta charset="utf-8">
<title>Pat Greene Self Storage Billboard</title>
<link rel="stylesheet" href="https://fonts.googleapis.com/css2?family=League+Spartan:wght@300;400;600;700;800&display=swap">
<style>
  :root {
    --navy: #1a2563;
    --red: #c8161d;
    --tan: #a8916f;
    --brown: #7b6a55;
    --white: #ffffff;
    --page: #ffffff;
    --ink: #111111;
  }
  html, body {
    margin: 0;
    padding: 0;
    width: 1200px;
    height: 1000px;
    overflow: hidden;
    background: var(--page);
    font-family: "League Spartan", sans-serif;
  }
  .billboard {
    position: absolute;
    left: 135px;
    top: 268px;
    width: 923px;
    height: 462px;
    background: var(--white);
    box-shadow: 0 0 3px rgba(0,0,0,0.25);
    overflow: hidden;
  }
  .billboard-art {
    position: absolute;
    left: 0;
    top: 0;
    width: 923px;
    height: 462px;
  }
  .address-label {
    position: absolute;
    left: 58px;
    top: 311px;
    width: 310px;
    color: var(--white);
    font-weight: 600;
    font-size: 25px;
    letter-spacing: 0.2px;
  }
  .rent-tag-text {
    position: absolute;
    left: 185px;
    top: 377px;
    width: 148px;
    color: var(--white);
    font-weight: 600;
    font-size: 21px;
    line-height: 22px;
    text-align: center;
  }
  .brand-name {
    position: absolute;
    left: 758px;
    top: 36px;
    width: 130px;
    display: flex;
    align-items: center;
    gap: 6px;
    color: var(--navy);
    font-weight: 700;
    font-size: 14px;
    line-height: 15px;
  }
  .brand-mark {
    width: 12px;
    height: 12px;
    background: var(--navy);
    flex: none;
  }
  .headline {
    position: absolute;
    left: 415px;
    top: 96px;
    margin: 0;
    color: var(--navy);
    font-weight: 800;
    font-size: 62px;
    line-height: 60px;
    letter-spacing: 1px;
  }
  .features {
    position: absolute;
    left: 420px;
    top: 226px;
    margin: 0;
    padding: 0;
    list-style: none;
    color: var(--ink);
    font-weight: 400;
    font-size: 26px;
    letter-spacing: 0.3px;
  }
  .features li {
    display: flex;
    align-items: center;
    gap: 6px;
    height: 39px;
  }
  .features svg { width: 22px; height: 22px; flex: none; }
  .contact {
    position: absolute;
    left: 418px;
    top: 368px;
    color: var(--navy);
    font-weight: 600;
  }
  .contact-row {
    display: flex;
    align-items: center;
    gap: 10px;
    height: 38px;
  }
  .contact-row svg { width: 25px; height: 25px; flex: none; }
  .contact-phone { font-size: 22px; }
  .contact-web { font-size: 25px; }
</style>
</head>
<body>
  <main class="billboard">
    <svg class="billboard-art" viewBox="0 0 923 462" xmlns="http://www.w3.org/2000/svg">
      <defs>
        <linearGradient id="photoTone" x1="0" y1="0" x2="1" y2="1">
          <stop offset="0" stop-color="#5f8a6e"/>
          <stop offset="0.45" stop-color="#c9b89a"/>
          <stop offset="1" stop-color="#4a4d52"/>
        </linearGradient>
        <linearGradient id="baseBand" x1="0" y1="0" x2="1" y2="0">
          <stop offset="0" stop-color="#1a2563"/>
          <stop offset="0.5" stop-color="#2a3566"/>
          <stop offset="1" stop-color="#8a7558"/>
        </linearGradient>
        <linearGradient id="baseFade" x1="0" y1="0" x2="0" y2="1">
          <stop offset="0" stop-color="#ffffff" stop-opacity="0"/>
          <stop offset="0.35" stop-color="#ffffff" stop-opacity="1"/>
        </linearGradient>
        <mask id="baseMask">
          <rect x="0" y="280" width="400" height="182" fill="url(#baseFade)"/>
        </mask>
        <clipPath id="leftPanel">
          <polygon points="0,0 278,0 362,462 0,462"/>
        </clipPath>
      </defs>

      <g clip-path="url(#leftPanel)">
        <rect class="facility-photo" role="img" aria-label="Photo of a row of storage units with green roll-up doors along a paved driveway" x="0" y="0" width="400" height="462" fill="url(#photoTone)"/>
        <rect x="0" y="280" width="400" height="182" fill="url(#baseBand)" mask="url(#baseMask)"/>
      </g>

      <polygon class="accent-stripe" points="278,0 305,0 386,462 360,462" fill="var(--tan)"/>

      <polygon class="direction-arrow" points="15,322 80,262 80,292 370,292 370,357 80,357 80,382" fill="var(--navy)" stroke="var(--tan)" stroke-width="6" stroke-linejoin="round"/>

      <polygon class="rent-tag" points="195,370 335,370 335,430 177,430" fill="var(--red)"/>

      <rect class="phone-device" role="img" aria-label="Smartphone showing the online rental website" x="336" y="339" width="52" height="105" rx="8" fill="#3a4256"/>
      <rect x="340" y="345" width="44" height="93" rx="5" fill="#d7dbe6"/>
    </svg>

    <div class="address-label">215 MAPLE RIDGE ROAD</div>
    <div class="rent-tag-text">Rent online anytime!</div>

    <div class="brand-name"><span class="brand-mark"></span>PAT GREENE SELF STORAGE</div>

    <h1 class="headline">SELF STORAGE<br>FACILITY</h1>

    <ul class="features">
      <li><svg viewBox="0 0 22 22"><rect x="1" y="3" width="18" height="18" rx="3" fill="var(--red)"/><path d="M5 11 l4 4 l11 -13" stroke="#ffffff" stroke-width="3" fill="none" stroke-linecap="round"/></svg>LARGE / SMALL UNITS</li>
      <li><svg viewBox="0 0 22 22"><rect x="1" y="3" width="18" height="18" rx="3" fill="var(--red)"/><path d="M5 11 l4 4 l11 -13" stroke="#ffffff" stroke-width="3" fill="none" stroke-linecap="round"/></svg>TEMPERATURE CONTROLLED</li>
      <li><svg viewBox="0 0 22 22"><rect x="1" y="3" width="18" height="18" rx="3" fill="var(--red)"/><path d="M5 11 l4 4 l11 -13" stroke="#ffffff" stroke-width="3" fill="none" stroke-linecap="round"/></svg>COVERED BOAT / RV PARKING</li>
    </ul>

    <div class="contact">
      <div class="contact-row contact-phone">
        <svg viewBox="0 0 24 24"><circle cx="12" cy="12" r="12" fill="var(--navy)"/><path d="M8 6 c-1.5 1 -1.5 3 0 5.5 c1.5 2.6 3.5 4.5 6 5.5 c1.5 0.6 2.6 0 3.2 -1 l-2.2 -2.2 l-1.8 1 c-1.5 -0.8 -2.8 -2.2 -3.6 -3.7 l1 -1.8 z" fill="#ffffff"/></svg>
        <span>555 014 2298</span>
      </div>
      <div class="contact-row contact-web">
        <svg viewBox="0 0 24 24" fill="none" stroke="var(--navy)" stroke-width="1.6"><circle cx="12" cy="12" r="10.5"/><ellipse cx="12" cy="12" rx="4.5" ry="10.5"/><line x1="1.5" y1="12" x2="22.5" y2="12"/><path d="M3.5 6.5 h17 M3.5 17.5 h17"/></svg>
        <span>www.patgreenestorage.com</span>
      </div>
    </div>
  </main>
</body>
</html>
```